Facial Tissue Brand Logo and Design

We would like you to design a Logo for the Facial Tissue Brand "Velora" along with the box design. The pack should indicate the pack size (150 x 2 ply). Also our company logo should be present (attached) along with a barcode. The box size dimensions should be 210mm (L) x 110mm (W) x 70mm (H). We are open to all kinds of nice designs which are attractive but not overdone. Happy designing!

UPDATE:
We appreciate the designs so far... but would also love to see more options in a simple and elegent design style that would look good on a table... please see attached below links for reference purpose:

www.pixmarrow.com/image-photo/cleaning-wipes-isolated-on-white-480215736

www.pixmarrow.com/image-photo/cleaning-wipes-isolated-on-white-692048153

www.pixmarrow.com/image-photo/delicate-female-hands-pulling-tissue-out-2875013649

Happy desgining!

We appreciate the designs so far.. but would like to to see some more options.

```html
<!DOCTYPE html>
<html lang="en">
<head>
<meta charset="utf-8">
<title>Velora Facial Tissue – Box Artwork</title>
<link href="https://fonts.googleapis.com/css2?family=Montserrat:wght@500;600;700&display=swap" rel="stylesheet">
<style>
  :root{
    --page:#ffffff;
    --cream:#f7f3e3;
    --cream-deep:#ece7d4;
    --gold:#c9ab63;
    --green:#2f6b34;
    --opening:#ffffff;
    --floral-a:#f3dcbc;
    --floral-b:#b9c2a6;
  }
  *{margin:0;padding:0;box-sizing:border-box}
  html,body{width:1200px;height:826px;overflow:hidden;background:var(--page)}
  body{position:relative;font-family:"Montserrat",sans-serif;color:var(--green)}

  .panel{position:absolute;overflow:hidden}
  .panel--top{left:56px;top:70px;width:714px;height:374px;
    background:linear-gradient(135deg,var(--cream),var(--cream-deep))}
  .panel--front{left:56px;top:444px;width:714px;height:238px;
    background:linear-gradient(90deg,var(--cream) 0%,#f9f5e6 50%,var(--cream-deep) 100%)}
  .panel--side{left:770px;top:444px;width:374px;height:238px;background:var(--gold)}

  .floral{position:absolute}
  .floral--wreath{left:40px;top:22px;width:634px;height:330px;border-radius:150px;
    background:radial-gradient(ellipse at center,rgba(243,220,188,.95) 30%,rgba(185,194,166,.75) 62%,rgba(185,194,166,0) 78%)}
  .floral--corner{left:0;top:0;width:230px;height:238px;
    background:radial-gradient(ellipse at 20% 0%,rgba(243,220,188,.95) 0%,rgba(185,194,166,.7) 45%,rgba(185,194,166,0) 72%)}
  .floral--edge{left:270px;top:0;width:420px;height:70px;
    background:radial-gradient(ellipse at 50% 0%,rgba(243,220,188,.85) 0%,rgba(185,194,166,.55) 45%,rgba(185,194,166,0) 75%)}

  .opening{position:absolute;left:112px;top:92px;width:490px;height:190px}
  .opening svg{position:absolute;inset:0}

  .brand{position:absolute;text-align:center}
  .brand__name{display:block;font-weight:600;letter-spacing:.04em;line-height:1;color:var(--green)}
  .brand__tag{display:block;font-weight:500;letter-spacing:.08em;margin-top:10px;color:var(--green);white-space:nowrap}

  .panel--top .brand{left:112px;top:140px;width:490px}
  .panel--top .brand__name{font-size:52px}
  .panel--top .brand__tag{font-size:15px}

  .panel--front .brand{left:260px;top:62px;width:340px}
  .panel--front .brand__name{font-size:56px}
  .panel--front .brand__tag{font-size:16px}

  .pack-size{position:absolute;right:24px;bottom:20px;font-weight:700;font-size:18px;letter-spacing:.02em}

  .panel--side .brand{left:0;top:70px;width:374px}
  .panel--side .brand__name{font-size:46px}
  .panel--side .brand__tag{font-size:12px;margin-top:8px}
</style>
</head>
<body>

  <section class="panel panel--top" aria-label="Box top">
    <div class="floral floral--wreath" role="img" aria-label="Watercolour wreath of cream roses and eucalyptus leaves"></div>
    <div class="opening">
      <svg width="490" height="190" viewBox="0 0 490 190">
        <rect x="2" y="2" width="486" height="186" rx="36" fill="var(--opening)"/>
        <rect x="12" y="12" width="466" height="166" rx="28" fill="none" stroke="var(--green)" stroke-width="1.4" stroke-dasharray="5 4"/>
      </svg>
    </div>
    <div class="brand">
      <span class="brand__name">Velora</span>
      <span class="brand__tag">FACIAL TISSUE | ULTRA SOFT</span>
    </div>
  </section>

  <section class="panel panel--front" aria-label="Box front">
    <div class="floral floral--corner" role="img" aria-label="Watercolour cluster of cream roses and green leaves"></div>
    <div class="floral floral--edge" role="img" aria-label="Trailing eucalyptus leaves along the top edge"></div>
    <div class="brand">
      <span class="brand__name">Velora</span>
      <span class="brand__tag">FACIAL TISSUE | ULTRA SOFT</span>
    </div>
    <p class="pack-size">150 x 2 ply</p>
  </section>

  <section class="panel panel--side" aria-label="Box end">
    <div class="brand">
      <span class="brand__name">Velora</span>
      <span class="brand__tag">FACIAL TISSUE | ULTRA SOFT</span>
    </div>
  </section>

</body>
</html>
```